Education Certificate

We need a modern yet professional Certificate for those who successfully pass / complete our online Training course.

There are various courses but ONE certificate design required.

the certificate needs to look extremely professional and of value.

```html
<!DOCTYPE html>
<html lang="en">
<head>
<meta charset="utf-8">
<title>Certificate of Completion</title>
<link href="https://fonts.googleapis.com/css2?family=Antonio:wght@600&family=Cormorant+Garamond:wght@500;600&family=Poppins:wght@400;600&family=Allura&display=swap" rel="stylesheet">
<style>
  :root {
    --backdrop: #45466d;
    --paper: #fbfbfd;
    --navy: #0d2a72;
    --gold: #e0b814;
    --ink: #1c1c22;
    --rule: #8a9cc8;
    --haze: rgba(190, 196, 218, 0.35);
  }
  * { margin: 0; padding: 0; box-sizing: border-box; }
  html, body { width: 805px; height: 1200px; overflow: hidden; }
  body { background: var(--backdrop); position: relative; }

  .certificate {
    position: absolute;
    left: 52px; top: 330px;
    width: 700px; height: 540px;
    background: var(--paper);
    overflow: hidden;
    box-shadow: 0 6px 18px rgba(0,0,0,0.25);
  }
  .certificate__backdrop { position: absolute; inset: 0; width: 100%; height: 100%; }
  .certificate__band {
    position: absolute; left: 0; right: 0; bottom: 0; height: 5px;
    background: var(--navy);
  }

  .brand {
    position: absolute; top: 46px; left: 0; right: 0;
    display: flex; align-items: center; justify-content: center; gap: 10px;
  }
  .brand__mark { width: 26px; height: 26px; background: var(--navy); }
  .brand__name {
    font-family: "Antonio", sans-serif; font-weight: 600;
    font-size: 34px; color: var(--navy); letter-spacing: 2px;
  }

  .institute {
    position: absolute; top: 135px; left: 0; right: 0; text-align: center;
    font-family: "Cormorant Garamond", serif; font-weight: 600;
    font-size: 21px; letter-spacing: 3.2px; color: var(--ink);
  }

  .title {
    position: absolute; top: 172px; left: 0; right: 0;
    display: flex; align-items: center; justify-content: center; gap: 8px;
  }
  .title__text {
    font-family: "Antonio", sans-serif; font-weight: 600;
    font-size: 52px; line-height: 1; letter-spacing: 3px; color: var(--navy);
  }
  .title__star { width: 32px; height: 32px; }

  .presented {
    position: absolute; top: 240px; left: 0; right: 0; text-align: center;
    font-family: "Poppins", sans-serif; font-weight: 600;
    font-size: 20px; letter-spacing: 3.5px; color: var(--ink);
  }

  .recipient {
    position: absolute; top: 262px; left: 0; right: 0; text-align: center;
    font-family: "Allura", cursive; font-size: 74px; line-height: 1.1;
    color: var(--gold);
  }

  .statement {
    position: absolute; top: 364px; left: 60px; right: 60px; text-align: center;
    font-family: "Poppins", sans-serif; font-weight: 400;
    font-size: 13px; line-height: 1.25; color: var(--ink);
  }

  .field {
    position: absolute; display: flex; align-items: flex-end; gap: 8px;
    font-family: "Cormorant Garamond", serif; font-weight: 500;
    font-size: 14px; letter-spacing: 0.4px; color: var(--gold);
  }
  .field__line { flex: 1; border-bottom: 1px solid var(--rule); margin-bottom: 4px; }
  .field--course { top: 426px; left: 56px; width: 561px; }
  .field--date { top: 470px; left: 56px; width: 240px; }
  .field--signature { top: 470px; left: 310px; width: 307px; }
</style>
</head>
<body>
  <main class="certificate">
    <svg class="certificate__backdrop" viewBox="0 0 700 540" preserveAspectRatio="none" aria-hidden="true">
      <polygon points="0,70 145,0 307,0 0,112" fill="var(--haze)"/>
      <polygon points="215,0 700,145 700,148 405,60 205,0" fill="var(--haze)"/>
      <polygon points="0,215 0,300 250,540 330,540" fill="var(--haze)"/>
      <polygon points="0,230 380,540 440,540 60,250" fill="rgba(190,196,218,0.25)"/>
      <polygon points="480,0 700,130 700,150 470,0" fill="rgba(190,196,218,0.3)"/>
      <line x1="0" y1="71" x2="145" y2="0" stroke="var(--navy)" stroke-width="1.6"/>
      <line x1="0" y1="112" x2="307" y2="0" stroke="var(--navy)" stroke-width="1.6"/>
      <line x1="525" y1="0" x2="700" y2="100" stroke="var(--navy)" stroke-width="1.6"/>
      <line x1="580" y1="0" x2="700" y2="81" stroke="var(--navy)" stroke-width="1.6"/>
    </svg>

    <div class="brand">
      <span class="brand__mark"></span>
      <span class="brand__name">MSEA</span>
    </div>

    <p class="institute">MERIDIAN SERVICE EXCELLENCE ACADEMY</p>

    <h1 class="title">
      <svg class="title__star" viewBox="0 0 24 24" aria-hidden="true"><polygon points="12,2 14.9,8.9 22.4,9.3 16.6,14.1 18.5,21.4 12,17.3 5.5,21.4 7.4,14.1 1.6,9.3 9.1,8.9" fill="var(--gold)"/></svg>
      <span class="title__text">CERTIFICATE OF COMPLETION</span>
      <svg class="title__star" viewBox="0 0 24 24" aria-hidden="true"><polygon points="12,2 14.9,8.9 22.4,9.3 16.6,14.1 18.5,21.4 12,17.3 5.5,21.4 7.4,14.1 1.6,9.3 9.1,8.9" fill="var(--gold)"/></svg>
    </h1>

    <p class="presented">PRESENTED TO</p>
    <p class="recipient">Amara Whitfield</p>

    <p class="statement">Lorem ipsum dolor sit amet, consectetur adipiscing elit, sed do eiusmod tempor<br>incididunt ut labore et dolore magna aliqua.</p>

    <div class="field field--course"><span>COURSE NAME</span><span class="field__line"></span></div>
    <div class="field field--date"><span>DATE</span><span class="field__line"></span></div>
    <div class="field field--signature"><span>SIGNATURE</span><span class="field__line"></span></div>

    <div class="certificate__band"></div>
  </main>
</body>
</html>
```